Wendell's UPDATE -Across the Board

Insurance Agent Business card and probably everything else !
Been in business for over 35 years and never took the time to update so really like the black-gold combo but open for suggestions (Honestly, I have NO idea how this works but sounds very cool ) Attached are two samples that I enjoy. The black and gold option is my favorite so looking for something like that!

```html
<!DOCTYPE html>
<html lang="en">
<head>
<meta charset="utf-8">
<title>Wendell S Marlow – Business Cards</title>
<link href="https://fonts.googleapis.com/css2?family=Libre+Baskerville:wght@400;700&display=swap" rel="stylesheet">
<style>
  :root{
    --backdrop:#141414;
    --card-black:#0b0b0b;
    --card-grey:#2c2c2c;
    --gold:#e2b453;
    --gold-light:#f6d27a;
    --gold-dark:#a9772a;
  }
  *{margin:0;padding:0;box-sizing:border-box}
  html,body{width:1200px;height:1200px;overflow:hidden;background:var(--backdrop)}
  .canvas{
    width:1200px;height:1200px;position:relative;
    display:flex;flex-direction:column;align-items:center;justify-content:center;gap:60px;
    font-family:"Libre Baskerville",Georgia,serif;
  }
  .card{
    width:840px;height:480px;position:relative;overflow:hidden;
    background:radial-gradient(ellipse at 55% 45%,var(--card-grey) 0%,var(--card-black) 70%);
    box-shadow:0 20px 50px rgba(0,0,0,.6);
  }

  /* soft gold decoration areas */
  .wave-area{position:absolute;inset:0;pointer-events:none}
  .card-contact .wave-area{
    background:
      radial-gradient(ellipse 70% 45% at 20% 100%,rgba(246,210,122,.85) 0%,rgba(226,180,83,.55) 40%,rgba(169,119,42,0) 100%),
      radial-gradient(ellipse 45% 40% at 95% 100%,rgba(246,210,122,.75) 0%,rgba(169,119,42,0) 100%);
  }
  .card-brand .wave-area{
    background:
      radial-gradient(ellipse 60% 65% at 0% 100%,rgba(246,210,122,.85) 0%,rgba(226,180,83,.55) 45%,rgba(169,119,42,0) 100%),
      radial-gradient(ellipse 55% 30% at 60% 100%,rgba(226,180,83,.5) 0%,rgba(169,119,42,0) 100%);
  }

  /* contact side */
  .contact-name{position:absolute;right:60px;top:48px;text-align:right}
  .contact-name h1{font-size:46px;font-weight:700;color:var(--gold);letter-spacing:1px}
  .contact-name p{font-size:19px;color:var(--gold);margin-top:6px}
  .contact-list{position:absolute;left:48px;top:170px;list-style:none;display:flex;flex-wrap:wrap;gap:12px 26px;width:740px}
  .contact-list li{display:flex;align-items:center;gap:8px;font-size:14px;color:var(--gold)}
  .contact-list li.wide{width:100%}
  .icon{width:20px;height:20px;flex:none}

  /* brand side */
  .brand-mark{position:absolute;left:60px;top:56px;display:flex;align-items:center;gap:12px}
  .brand-mark .dot{width:26px;height:26px;border:2px solid var(--gold)}
  .brand-mark span{font-size:40px;color:var(--gold);letter-spacing:2px}
  .brand-title{position:absolute;right:60px;top:150px;text-align:right;color:var(--gold)}
  .brand-title .sub{font-size:30px}
  .brand-title .main{font-size:76px;line-height:1.05}
  .brand-title .est{font-size:22px;margin-top:6px}
</style>
</head>
<body>
<main class="canvas">

  <section class="card card-contact" aria-label="Contact side">
    <div class="wave-area" role="img" aria-label="Flowing gold wave decoration along the lower part of the card"></div>
    <div class="contact-name">
      <h1>Wendell S Marlow</h1>
      <p>Insurance &amp; Financial Consultant</p>
    </div>
    <ul class="contact-list">
      <li><svg class="icon" viewBox="0 0 20 20"><circle cx="10" cy="10" r="9" fill="none" stroke="var(--gold)"/><path d="M7 6l2 2-1 1.5 2.5 2.5 1.5-1 2 2-1.5 1.5C9 14 6 11 5.5 7.5Z" fill="var(--gold)"/></svg>954-555-0173</li>
      <li><svg class="icon" viewBox="0 0 20 20"><circle cx="10" cy="10" r="9" fill="none" stroke="var(--gold)"/><rect x="6" y="6" width="8" height="8" rx="1" fill="var(--gold)"/></svg>954-555-0186</li>
      <li><svg class="icon" viewBox="0 0 20 20"><circle cx="10" cy="10" r="9" fill="none" stroke="var(--gold)"/><rect x="5.5" y="7" width="9" height="6" fill="none" stroke="var(--gold)"/><path d="M5.5 7l4.5 3.5L14.5 7" fill="none" stroke="var(--gold)"/></svg>wendell@wsminsures.com</li>
      <li><svg class="icon" viewBox="0 0 20 20"><circle cx="10" cy="10" r="9" fill="none" stroke="var(--gold)"/><circle cx="10" cy="10" r="4.5" fill="none" stroke="var(--gold)"/><path d="M5.5 10h9M10 5.5v9" stroke="var(--gold)"/></svg>www.wsminsures.com</li>
      <li class="wide"><svg class="icon" viewBox="0 0 20 20"><circle cx="10" cy="10" r="9" fill="none" stroke="var(--gold)"/><path d="M10 15s-3.5-3.5-3.5-6a3.5 3.5 0 0 1 7 0c0 2.5-3.5 6-3.5 6Z" fill="var(--gold)"/></svg>4120 Harbor Lane, Suite 210, Coral Glen, FL 33000</li>
    </ul>
  </section>

  <section class="card card-brand" aria-label="Brand side">
    <div class="wave-area" role="img" aria-label="Flowing gold wave decoration sweeping across the lower left of the card"></div>
    <div class="brand-mark"><i class="dot"></i><span>WSM</span></div>
    <div class="brand-title">
      <p class="sub">Insurance &amp; Financial</p>
      <p class="main">Consultant</p>
      <p class="est">Est. 1985</p>
    </div>
  </section>

</main>
</body>
</html>
```